Varbek - Nutritious Snacks and Desserts

We need a creative e-commerce website in which all features--buttons, background, etc.--convey our message: We sell delicious, nutritious snacks and desserts that most closely comply with the paleo diet guidelines. Our first product is Brunavo®--raw, vegan, paleo chocolate balls that are made of dates, coconut, and cocoa. Our products are organic, raw, irresistible and nutritious. We have several versions of Brunavo® in development, as well as mousse, ice cream, and crackers. Our mission is to purvey basic healthy foods. Our motto is, "Fuel for the Daily Trail-Seeker(tm)."

Target Market(s)

Health-conscious professionals who tend to shop at health food stores. Our products also meet the requirements of a gluten-free diet; and they also don't contain refined sugar, so shoppers with gluten and possibly sugar issues are incidental customers.

Industry/Entity Type

Health Product

Coding

Coded - Design and coding required

Number of Pages Required

5+ page

Colors

Designer to choose colors to be used in the design.

Requirements
Must have
• We need at least a home page, a products page, an about-us page, a contact page, and a shopping cart page. We would like to be able to add products on our own later. We should be able to handle some basic coding, especially if it's just a matter of copying and modifying product pages. We would also like the ability in the future to add blogging pages, allowing us to write articles about health food and healthy lifestyle, thus attracting web-traffic (SEO).
• Other features we would like to have:
• Product photo slider on the hopepage
• Back-to-top button at the bottom of the home page
• Make sure the site is mobile-compatible
• A search bar at the top of the homepage
• "Create an account" and "Previous orders"--allowing customers to see their previous orders and reorder what they purchased in the past.
Nice to have
• We would like to convey the paleo theme without actually stating it anywhere. We'll add text as necessary, according to the page layout; you can use ipsum lorem for purpose of demonstration.

```html
<!DOCTYPE html>
<html lang="en">
<head>
<meta charset="utf-8">
<title>Varbek Foods</title>
<link href="https://fonts.googleapis.com/css2?family=Montserrat:wght@400;500;600;700;800&family=Open+Sans:wght@400;600&family=Yellowtail&family=Amatic+SC:wght@700&display=swap" rel="stylesheet">
<style>
:root{
  --green:#5aa51a;
  --green-bright:#6cc400;
  --green-dark:#3f7d12;
  --green-deep:#4a8f16;
  --ink:#2b2b2b;
  --grey:#555;
  --grey-light:#8a8a8a;
  --paper:#f3f3f3;
  --white:#fff;
  --night:#1f2420;
}
*{margin:0;padding:0;box-sizing:border-box}
html,body{width:1200px;height:3141px;overflow:hidden}
body{position:relative;font-family:"Open Sans",Arial,sans-serif;color:var(--ink);background:var(--paper)}
.abs{position:absolute}
.script{font-family:"Yellowtail",cursive;color:var(--green-bright);font-weight:400}
.heading{font-family:"Montserrat",Arial,sans-serif;font-weight:800;letter-spacing:1px}

/* top bar */
.topbar{left:0;top:0;width:1200px;height:29px;background:var(--green);color:var(--white);font-size:12px;font-family:"Montserrat",sans-serif}
.topbar span{position:absolute;top:7px;display:flex;align-items:center;gap:6px}
.topbar svg{width:12px;height:12px}

/* header */
.header{left:0;top:29px;width:1200px;height:134px;background:var(--white)}
.brand{left:115px;top:40px;display:flex;align-items:center;gap:10px}
.brand-dot{width:34px;height:34px;border-radius:50%;background:var(--green-bright)}
.brand-name{font-family:"Montserrat",sans-serif;font-weight:700;font-size:34px;color:var(--green)}
.nav{left:310px;top:63px;display:flex;gap:0;font-family:"Montserrat",sans-serif;font-size:13px;color:var(--ink)}
.nav a{color:var(--ink);text-decoration:none;position:absolute;white-space:nowrap}
.nav i{position:absolute;width:5px;height:5px;border-radius:50%;background:var(--green-bright);top:6px}
.header-tools{left:995px;top:55px}
.cart-count{left:1063px;top:53px;width:16px;height:16px;border-radius:50%;background:var(--green);color:#fff;font-size:9px;text-align:center;line-height:16px}

/* hero */
.hero{left:0;top:163px;width:1200px;height:444px;background:linear-gradient(120deg,#2f2f2c 0%,#4a4237 40%,#2a2a27 70%,#1c1c1a 100%)}
.hero-shade{left:0;top:163px;width:1200px;height:444px;background:rgba(0,0,0,.35)}
.hero-title{left:0;width:1200px;text-align:center;color:var(--white)}
.hero-title.l1{top:250px;font-size:68px}
.hero-title.l2{top:325px;font-size:82px;color:var(--green-bright)}
.hero-tag{left:0;top:425px;width:1200px;text-align:center;color:var(--white);font-size:19px}
.btn{display:flex;align-items:center;justify-content:space-between;font-family:"Montserrat",sans-serif;font-weight:600;font-size:11px;letter-spacing:.5px;color:#fff;background:var(--green-bright);padding:0 16px}
.hero-btn{left:528px;top:473px;width:148px;height:38px}
.dots-v{left:1143px;top:352px}
.dots-v i{display:block;width:9px;height:9px;border-radius:50%;border:1.5px solid #fff;margin-bottom:9px}
.dots-v i.on{background:#fff}
.hero-dot{left:594px;top:555px;width:10px;height:10px;border-radius:50%;background:#fff}

/* products */
.section-script{left:0;width:1200px;text-align:center;font-size:40px}
.section-title{left:0;width:1200px;text-align:center;font-size:42px;color:#6b6b6b}
.title-rule{left:560px;width:80px;height:3px;background:var(--green-bright)}
.product-photo{left:207px;top:789px;width:419px;height:415px;background:linear-gradient(150deg,#9a9a8e,#d8d2c2 45%,#7f7d72)}
.slide-arrow{top:953px;width:59px;height:56px;background:#cfcfcf}
.deal-card{left:605px;top:810px;width:436px;height:373px;background:#fff;box-shadow:0 2px 10px rgba(0,0,0,.12);text-align:center}
.deal-card .script{position:absolute;left:0;width:100%;top:22px;font-size:36px;line-height:1}
.deal-card .heading{position:absolute;left:0;width:100%;top:52px;font-size:38px;color:#6b6b6b}
.deal-rule{position:absolute;left:158px;top:103px;width:120px}
.deal-name{position:absolute;left:0;width:100%;top:122px;font-family:"Montserrat",sans-serif;font-weight:700;font-size:18px;letter-spacing:1px}
.stars{position:absolute;left:0;width:100%;top:147px;color:var(--green-bright);font-size:16px;letter-spacing:1px}
.price{position:absolute;left:0;width:100%;top:172px;font-family:"Montserrat",sans-serif;font-weight:700;font-size:21px;color:var(--green)}
.deal-desc{position:absolute;left:80px;width:276px;top:218px;font-size:11.5px;line-height:15px;color:var(--grey)}
.deal-btn{position:absolute;left:161px;top:308px;width:141px;height:36px}
.treeline{left:0;top:1204px;width:1200px;height:84px;background:linear-gradient(180deg,rgba(90,165,26,0) 0%,rgba(90,165,26,.35) 60%,var(--green) 100%)}

/* about */
.about-band{left:0;top:1288px;width:1200px;height:262px;background:var(--green)}
.about-script{color:#d9f2b8}
.about-title{color:#fff}
.about-card{left:98px;top:1432px;width:1003px;height:478px;background:#fff;box-shadow:0 3px 14px rgba(0,0,0,.12)}
.about-head{left:186px;top:1478px;font-family:"Amatic SC",cursive;font-size:48px;line-height:48px;color:var(--green-dark)}
.about-text{left:186px;top:1615px;width:414px;font-size:13px;line-height:20px;color:var(--grey)}
.about-btn{left:186px;top:1811px;width:166px;height:38px}
.about-photo{left:653px;top:1482px;width:321px;height:371px;border-radius:50%;background:radial-gradient(circle at 50% 55%,#c8a46a 0%,#8a6b3e 30%,#2d2d2a 62%,#1c1c1a 100%)}

/* blog */
.blog-card{top:2073px;width:302px;height:450px;background:#fff;border:1px solid #d6d6d6}
.blog-date{position:absolute;right:14px;top:14px;font-size:10px;font-family:"Montserrat",sans-serif;color:var(--grey)}
.blog-photo{position:absolute;left:0;top:42px;width:300px;height:157px;background:linear-gradient(135deg,#4b3a2c,#8c8a5a 40%,#e6e3da 60%,#5a4633)}
.blog-title{position:absolute;left:16px;top:222px;font-family:"Montserrat",sans-serif;font-weight:700;font-size:12px;letter-spacing:1px;color:var(--green)}
.blog-cat{position:absolute;left:16px;top:242px;font-size:10px;color:var(--grey-light);letter-spacing:.5px}
.blog-text{position:absolute;left:16px;top:290px;width:268px;font-size:12px;line-height:20px;color:var(--grey)}
.blog-more{position:absolute;left:16px;top:389px;width:86px;height:41px;border:1px solid var(--green);color:var(--green);font-size:9px;font-family:"Montserrat",sans-serif;letter-spacing:1px;text-align:center;line-height:39px}
.blog-share{position:absolute;right:14px;top:400px;display:flex;gap:4px}
.blog-share i{width:19px;height:19px;border-radius:50%;background:var(--green-bright)}
.pager{top:2566px;width:40px;height:3px;background:#c9c9c9}
.pager.on{background:var(--green-bright)}

/* footer */
.foot-left{left:0;top:2609px;width:599px;height:459px;background:var(--green)}
.foot-right{left:599px;top:2609px;width:601px;height:459px;background:linear-gradient(135deg,#2c302a,#4a4a3e 50%,#23271f)}
.foot-right-shade{left:599px;top:2609px;width:601px;height:459px;background:rgba(15,20,15,.55)}
.assist{left:0;top:2763px;width:599px;text-align:center;color:#fff;font-size:14px}
.phone-box{left:172px;top:2819px;width:391px;height:88px;border:3px solid #fff;color:#fff;font-family:"Montserrat",sans-serif;font-weight:600;font-size:48px;text-align:center;line-height:82px}
.address{left:0;top:2990px;width:599px;text-align:center;color:#fff;font-size:13px;line-height:18px;font-family:"Montserrat",sans-serif}
.contact-kicker{left:599px;top:2678px;width:601px;text-align:center;color:#fff;font-size:10px;letter-spacing:5px;font-family:"Montserrat",sans-serif}
.contact-title{left:599px;top:2696px;width:601px;text-align:center;color:var(--green-bright);font-family:"Montserrat",sans-serif;font-weight:700;font-size:27px;letter-spacing:1px}
.field{left:637px;width:393px;background:rgba(255,255,255,.78);color:#333;font-size:12px;padding:8px 10px}
.submit{left:637px;top:2969px;width:393px;height:34px;justify-content:center;gap:10px;font-size:12px}
.bottombar{left:0;top:3068px;width:1200px;height:73px;background:var(--green-dark)}
.copyright{left:117px;top:3097px;color:#fff;font-size:12px}
.foot-social{left:962px;top:3098px;display:flex;gap:22px}
.foot-social i{width:12px;height:12px;border-radius:50%;background:#fff}
</style>
</head>
<body>

<div class="abs topbar">
  <span style="left:119px"><svg viewBox="0 0 24 24"><circle cx="12" cy="12" r="12" fill="#fff"/><path d="M8 6l2 0 1 3-1.5 1a8 8 0 004 4l1-1.5 3 1v2c0 1-1 2-2 2A11 11 0 016 8c0-1 1-2 2-2z" fill="#5aa51a"/></svg>(123) 456 - 7890</span>
  <span style="left:775px"><svg viewBox="0 0 24 24"><circle cx="12" cy="8" r="5" fill="#fff"/><path d="M3 23c0-6 4-9 9-9s9 3 9 9z" fill="#fff"/></svg>Login / Sign up</span>
  <span style="left:894px"><svg viewBox="0 0 24 24"><path d="M12 21L3 12a5 5 0 019-6 5 5 0 019 6z" fill="#fff"/></svg>Wishlist (0)</span>
  <span style="left:1001px"><svg viewBox="0 0 24 24" fill="none" stroke="#fff" stroke-width="2"><path d="M2 3h3l3 12h11l2-8H7"/><circle cx="9" cy="20" r="1.5"/><circle cx="18" cy="20" r="1.5"/></svg>Checkout</span>
</div>

<header class="abs header">
  <div class="abs brand"><div class="brand-dot"></div><div class="brand-name">Varbek</div></div>
  <nav class="abs nav">
    <a style="left:0">HOME</a><i style="left:76px"></i>
    <a style="left:117px">ABOUT US</a><i style="left:223px"></i>
    <a style="left:262px">PRODUCTS</a><i style="left:375px"></i>
    <a style="left:414px">BLOG</a><i style="left:483px"></i>
    <a style="left:527px">CONTACT US</a>
  </nav>
  <svg class="abs header-tools" width="80" height="30" viewBox="0 0 80 30" fill="none" stroke="#555" stroke-width="2">
    <circle cx="11" cy="11" r="8"/><path d="M17 17l7 7"/>
    <path d="M54 9h18l-2 16H56z"/><path d="M58 9a5 5 0 0110 0"/>
  </svg>
</header>
<div class="abs cart-count">2</div>

<section>
  <div class="abs hero" role="img" aria-label="Photo of a plated healthy dish with chopsticks on a dark wooden table"></div>
  <div class="abs hero-shade"></div>
  <h1 class="abs heading hero-title l1">WELCOME TO</h1>
  <h1 class="abs heading hero-title l2">VARBEK FOODS.</h1>
  <p class="abs hero-tag">Fuel for the Daily Trail-Seeker<sup style="font-size:11px">TM</sup></p>
  <a class="abs btn hero-btn">GET STARTED <span>&rarr;</span></a>
  <div class="abs dots-v"><i></i><i class="on"></i><i></i><i></i></div>
  <div class="abs hero-dot"></div>
</section>

<section>
  <div class="abs script section-script" style="top:640px">My Popular</div>
  <h2 class="abs heading section-title" style="top:682px">PRODUCTS</h2>
  <div class="abs title-rule" style="top:740px"></div>

  <div class="abs slide-arrow" style="left:0"><svg width="59" height="56"><path d="M36 16L24 28l12 12" stroke="#fff" stroke-width="3" fill="none"/></svg></div>
  <div class="abs slide-arrow" style="left:1141px"><svg width="59" height="56"><path d="M23 16l12 12-12 12" stroke="#fff" stroke-width="3" fill="none"/></svg></div>

  <div class="abs product-photo" role="img" aria-label="Product photo of a Brunavo dessert cup on a tiled counter"></div>

  <div class="abs deal-card">
    <div class="script">Daily</div>
    <div class="heading">DEALS</div>
    <svg class="deal-rule" height="10" viewBox="0 0 120 10"><path d="M0 5h48M72 5h48" stroke="#bbb"/><rect x="55" y="1" width="10" height="8" fill="none" stroke="#bbb"/></svg>
    <div class="deal-name">BRUNAVO&reg;</div>
    <div class="stars">&#9733;&#9733;&#9733;&#9733;&#9733;</div>
    <div class="price">$80.00</div>
    <p class="deal-desc">Our products are raw, organic, vegan, gluten-free, dairy-free, fiber-rich, nutrient-dense, antioxidant-rich real foods with no preservatives, no added sugar, and no artificial or plant-based sweeteners. And they are irresistibly scrumptious!</p>
    <a class="btn deal-btn">ADD TO CART <svg width="16" height="16" viewBox="0 0 24 24" fill="none" stroke="#fff" stroke-width="2"><path d="M4 8h16l-2 13H6z"/><path d="M9 8a3 3 0 016 0"/></svg></a>
  </div>
  <div class="abs treeline" role="img" aria-label="Silhouette row of trees and wind turbines"></div>
</section>

<section>
  <div class="abs about-band"></div>
  <div class="abs script section-script about-script" style="top:1318px">About</div>
  <h2 class="abs heading section-title about-title" style="top:1356px;font-size:40px">VARBEK FOOD</h2>
  <div class="abs about-card"></div>
  <svg class="abs" style="left:580px;top:1416px" width="40" height="18"><path d="M0 16L20 0l20 16z" fill="#fff"/></svg>
  <h3 class="abs about-head">FUEL FOR THE<br>DAILY TRAIL-SEEKER</h3>
  <svg class="abs" style="left:186px;top:1585px" width="44" height="4"><rect width="44" height="2" fill="#bbb"/></svg>
  <p class="abs about-text">Lorem Ipsum is simply dummy text of the printing and typesetting industry. Lorem Ipsum has been the industry's standard dummy text ever since the 1500s, when an unknown printer took a galley of type and scrambled it to make a type specimen book. It has survived not only five centuries, but also the leap into electronic typesetting, remaining essentially unchanged. It was popularised in the 1960s with the release of Letraset sheets containing Lorem Ipsum passages.</p>
  <a class="abs btn about-btn">READ MORE <span>&rarr;</span></a>
  <div class="abs about-photo" role="img" aria-label="Photo of a pancake stack topped with cream and blueberries"></div>
</section>

<section>
  <div class="abs script section-script" style="top:1932px">Latest from</div>
  <h2 class="abs heading section-title" style="top:1972px">THE BLOG</h2>
  <div class="abs title-rule" style="top:2030px"></div>

  <article class="abs blog-card" style="left:117px">
    <div class="blog-date">MAY 10, 2018, WEDNESDAY</div>
    <div class="blog-photo" role="img" aria-label="Photo of a salad plate with grilled flatbread"></div>
    <div class="blog-title">LOREM IPSUM DOLOR SIT AMET</div>
    <div class="blog-cat">FOOD / PORTFOLIO</div>
    <p class="blog-text">Lorem ipsum dolor sit amet, consectetur adipiscing elit. Sed euismod in tellus in mattis. Aliquam erat volutpat. Praesent ultricies aliquet erat a semper.</p>
    <a class="blog-more">READ MORE</a>
    <div class="blog-share"><i></i><i></i><i></i><i></i></div>
  </article>
  <article class="abs blog-card" style="left:448px">
    <div class="blog-date">MAY 10, 2018, WEDNESDAY</div>
    <div class="blog-photo" role="img" aria-label="Photo of a salad plate with grilled flatbread"></div>
    <div class="blog-title">LOREM IPSUM DOLOR SIT AMET</div>
    <div class="blog-cat">FOOD / PORTFOLIO</div>
    <p class="blog-text">Lorem ipsum dolor sit amet, consectetur adipiscing elit. Sed euismod in tellus in mattis. Aliquam erat volutpat. Praesent ultricies aliquet erat a semper.</p>
    <a class="blog-more">READ MORE</a>
    <div class="blog-share"><i></i><i></i><i></i><i></i></div>
  </article>
  <article class="abs blog-card" style="left:779px">
    <div class="blog-date">MAY 10, 2018, WEDNESDAY</div>
    <div class="blog-photo" role="img" aria-label="Photo of a salad plate with grilled flatbread"></div>
    <div class="blog-title">LOREM IPSUM DOLOR SIT AMET</div>
    <div class="blog-cat">FOOD / PORTFOLIO</div>
    <p class="blog-text">Lorem ipsum dolor sit amet, consectetur adipiscing elit. Sed euismod in tellus in mattis. Aliquam erat volutpat. Praesent ultricies aliquet erat a semper.</p>
    <a class="blog-more">READ MORE</a>
    <div class="blog-share"><i></i><i></i><i></i><i></i></div>
  </article>
  <div class="abs pager on" style="left:528px"></div>
  <div class="abs pager" style="left:579px"></div>
  <div class="abs pager" style="left:630px"></div>
</section>

<footer>
  <div class="abs foot-left"></div>
  <div class="abs foot-right" role="img" aria-label="Dimmed photo of a dinner table with plated food"></div>
  <div class="abs foot-right-shade"></div>

  <svg class="abs" style="left:330px;top:2692px" width="64" height="64" viewBox="0 0 64 64" fill="#fff">
    <path d="M14 10l10 0 4 12-6 5a30 30 0 0015 15l5-6 12 4v10c0 3-3 5-6 5A44 44 0 019 16c0-3 2-6 5-6z"/>
    <path d="M38 8a20 20 0 0118 18" stroke="#fff" stroke-width="4" fill="none"/>
    <path d="M38 18a10 10 0 018 8" stroke="#fff" stroke-width="4" fill="none"/>
  </svg>
  <p class="abs assist">24/7 Assistance. Call us any time.</p>
  <div class="abs phone-box">(123) 456-789</div>
  <svg class="abs" style="left:349px;top:2946px" width="30" height="30" viewBox="0 0 30 30" fill="none" stroke="#fff" stroke-width="2">
    <rect x="1" y="1" width="28" height="28"/><path d="M15 23s-6-6-6-10a6 6 0 0112 0c0 4-6 10-6 10z"/><circle cx="15" cy="13" r="2"/>
  </svg>
  <p class="abs address">48 ORCHARD LN<br>FERNHILL, FL 32910</p>

  <div class="abs contact-kicker">CONTACT US</div>
  <h2 class="abs contact-title">GIVE US A SHOUT</h2>
  <div class="abs field" style="top:2806px;height:34px">Enter Name</div>
  <div class="abs field" style="top:2850px;height:33px">Enter Email</div>
  <div class="abs field" style="top:2894px;height:63px">Enter Message</div>
  <a class="abs btn submit">SUBMIT <span>&rarr;</span></a>

  <div class="abs bottombar"></div>
  <p class="abs copyright">&copy; 2018 Varbek Foods , All Right Reserved.</p>
  <div class="abs foot-social"><i></i><i></i><i></i><i></i></div>
</footer>

</body>
</html>
```